bluecastle aquatics of northeast florida business card

I need a new attractive business card. I am planning on printing on very thick rounded corner stock and having painted edges. We are a swimming pool remodel, repair, and service company in north florida. Our current logo is red, white, and blue. It doesn't necessarily have to stay that way, I am open to other ideas. It will need to contain my name, work and cell numbers, email, website, and my contractor license number.

Target Market(s)

High end residential and commercial clients

Industry/Entity Type

Business

Contact Information for Business Card

Company name, employee name and title, work and cell phone numbers, email and website, and Contractor number.

our work scope should be on card somewhere: remodel ~ repair ~ service

logo or slight variation of logo also. (not necessarily set on keeping exact logo)

Colors

Designer to choose colors to be used in the design.

Requirements
Nice to have
• We deal with water so I think some sort of water element or just a color similar to pool water would be nice to integrate into design.

```html
<!DOCTYPE html>
<html lang="en">
<head>
<meta charset="utf-8">
<title>Bluecastle Aquatics – Business Card</title>
<link rel="stylesheet" href="https://fonts.googleapis.com/css2?family=Crimson+Pro:wght@400;500&family=Roboto:wght@400&display=swap">
<style>
  :root {
    --page-bg: #efefef;
    --brand-blue: #0079bb;
    --brand-red: #d9393b;
    --card-back: #f9f9f9;
    --ink: #333333;
    --white: #ffffff;
  }
  html, body {
    margin: 0;
    width: 1200px;
    height: 929px;
    overflow: hidden;
    background: var(--page-bg);
  }
  .card {
    position: absolute;
    left: 374px;
    width: 451px;
    height: 272px;
    box-sizing: border-box;
  }
  .card--front {
    top: 176px;
    background: var(--brand-blue);
    color: var(--white);
  }
  .card--back {
    top: 480px;
    background: var(--card-back);
  }
  .front-brand {
    position: absolute;
    left: 0;
    right: 0;
    top: 108px;
    display: flex;
    justify-content: center;
    align-items: center;
    gap: 12px;
  }
  .front-brand__mark {
    width: 42px;
    height: 42px;
    background: var(--white);
    border-radius: 5px;
    flex: none;
  }
  .front-brand__name {
    font-family: "Crimson Pro", serif;
    color: var(--white);
    line-height: 1;
    text-transform: uppercase;
  }
  .front-brand__main {
    display: block;
    font-weight: 500;
    font-size: 25px;
    letter-spacing: 0.3px;
  }
  .front-brand__sub {
    display: block;
    font-weight: 400;
    font-size: 12.5px;
    letter-spacing: 3.6px;
    margin-top: 2px;
  }
  .front-tagline {
    position: absolute;
    left: 0;
    right: 0;
    top: 242px;
    margin: 0;
    text-align: center;
    font-family: "Roboto", sans-serif;
    font-size: 12px;
    line-height: 14px;
    color: var(--white);
  }
  .back-brand {
    position: absolute;
    left: 46px;
    top: 92px;
    width: 130px;
    text-align: center;
  }
  .back-brand__mark {
    width: 64px;
    height: 64px;
    margin: 0 auto 10px;
    background: var(--brand-red);
    border-radius: 6px;
  }
  .back-brand__name {
    font-family: "Crimson Pro", serif;
    font-weight: 500;
    font-size: 15px;
    line-height: 1.15;
    color: var(--brand-red);
    text-transform: uppercase;
  }
  .contact {
    position: absolute;
    left: 240px;
    top: 56px;
    font-family: "Roboto", sans-serif;
    color: var(--ink);
  }
  .contact__name {
    font-family: "Crimson Pro", serif;
    font-weight: 400;
    font-size: 19px;
    color: var(--brand-blue);
    margin: 0;
    line-height: 1.1;
  }
  .contact__title {
    font-size: 11px;
    margin: 1px 0 0;
  }
  .contact__address {
    font-size: 11.5px;
    line-height: 15px;
    margin: 16px 0 6px;
    font-style: normal;
  }
  .contact__list {
    list-style: none;
    margin: 0;
    padding: 0;
    font-size: 11.5px;
  }
  .contact__item {
    display: flex;
    align-items: center;
    height: 15.5px;
  }
  .contact__icon {
    width: 10px;
    height: 10px;
    margin-right: 13px;
    fill: var(--brand-blue);
    flex: none;
  }
  .contact__label {
    color: var(--brand-blue);
    margin-right: 4px;
  }
</style>
</head>
<body>
  <section class="card card--front">
    <div class="front-brand">
      <span class="front-brand__mark"></span>
      <span class="front-brand__name">
        <span class="front-brand__main">Bluecastle Aquatics</span>
        <span class="front-brand__sub">of Northeast Florida</span>
      </span>
    </div>
    <p class="front-tagline">swimming pool remodel, repair, and service</p>
  </section>

  <section class="card card--back">
    <div class="back-brand">
      <div class="back-brand__mark"></div>
      <div class="back-brand__name">Bluecastle Aquatics</div>
    </div>
    <div class="contact">
      <h1 class="contact__name">Daniel Reyes</h1>
      <p class="contact__title">Director</p>
      <address class="contact__address">123, Your city Name,<br>Street No. 113, Country 123456</address>
      <ul class="contact__list">
        <li class="contact__item">
          <svg class="contact__icon" viewBox="0 0 10 10" aria-hidden="true"><path d="M0 3.5C2-0.5 8-0.5 10 3.5L8 4.5 7 3H3L2 4.5Z M2 5H8L9 9H1Z"/></svg>
          <span class="contact__label">W</span>000-555-0142
        </li>
        <li class="contact__item">
          <svg class="contact__icon" viewBox="0 0 10 10" aria-hidden="true"><path d="M0 3.5C2-0.5 8-0.5 10 3.5L8 4.5 7 3H3L2 4.5Z M2 5H8L9 9H1Z"/></svg>
          <span class="contact__label">C</span>000-555-0187
        </li>
        <li class="contact__item">
          <svg class="contact__icon" viewBox="0 0 10 10" aria-hidden="true"><path d="M0 2H10V8H0Z M0.8 2.6 5 5.6 9.2 2.6" fill="none" stroke="#0079bb" stroke-width="1.2"/></svg>
          daniel@bluecastleaquatics.com
        </li>
        <li class="contact__item">
          <svg class="contact__icon" viewBox="0 0 10 10" aria-hidden="true"><g fill="none" stroke="#0079bb" stroke-width="0.9"><circle cx="5" cy="5" r="4.4"/><ellipse cx="5" cy="5" rx="2" ry="4.4"/><path d="M0.6 5H9.4 M1.3 2.8H8.7 M1.3 7.2H8.7"/></g></svg>
          www.bluecastleaquatics.com
        </li>
        <li class="contact__item">
          <svg class="contact__icon" viewBox="0 0 10 10" aria-hidden="true"><path d="M1.5 5.2 4 7.7 8.8 2.3" fill="none" stroke="#0079bb" stroke-width="1.4"/></svg>
          Contractor Lic. # CPC1459876
        </li>
      </ul>
    </div>
  </section>
</body>
</html>
```